KELTO Robotics Engineering Design Team - Pull Up Banner Design

I need a pull-up banner design which I can use at trade shows and events to market our research and development group. We are specialist design engineers who have expertise in:
- Embedded Electronics and Circuit Design
- Rapid Functional Prototyping
- Sensor and Vision Systems
- Robotics Systems

Recent projects include:
- Robotic concrete sewer probes
- IoT wildlife tracking systems
- Robots for exploring wombat burrows
- Smart pest control technology

Target Market(s)

Potential clients who want us to design a project for them

Industry/Entity Type

Engineering Consulting

Colors

Designer to choose colors to be used in the design.

Requirements
Must have
• Look professional and have a high-tech feel to it

```html
<!DOCTYPE html>
<html lang="en">
<head>
<meta charset="utf-8">
<title>KELTO Pull Up Banner</title>
<link href="https://fonts.googleapis.com/css2?family=Michroma&family=Saira+Semi+Condensed:wght@400;500&display=swap" rel="stylesheet">
<style>
  :root {
    --brand-blue: #33479a;
    --brand-red: #bf323c;
    --stripe-white: #ffffff;
    --grommet: #2a2a33;
    --page-bg: #eceef1;
    --photo-sky: #c9d3dc;
    --photo-mid: #8a8f6e;
    --photo-ground: #5d6a3c;
  }
  html, body {
    margin: 0;
    padding: 0;
    width: 1164px;
    height: 1200px;
    overflow: hidden;
    background: var(--page-bg);
  }
  .banner {
    position: absolute;
    left: 394px;
    top: 10px;
    width: 376px;
    height: 1180px;
    display: block;
  }
  .brand-name {
    font-family: "Michroma", "Saira Semi Condensed", sans-serif;
    font-size: 46px;
    fill: var(--stripe-white);
    letter-spacing: 4px;
  }
  .tagline, .services, .projects, .web-address {
    font-family: "Saira Semi Condensed", sans-serif;
    fill: var(--stripe-white);
  }
  .tagline { font-size: 14px; font-weight: 500; letter-spacing: 0.3px; }
  .web-address { font-size: 19px; font-weight: 500; }
  .services { font-size: 20px; font-weight: 400; }
  .projects { font-size: 19px; font-weight: 400; }
</style>
</head>
<body>
<svg class="banner" viewBox="0 0 376 1180" xmlns="http://www.w3.org/2000/svg">
  <defs>
    <linearGradient id="photoTones" x1="0" y1="0" x2="0" y2="1">
      <stop offset="0" stop-color="var(--photo-sky)"/>
      <stop offset="0.45" stop-color="var(--photo-mid)"/>
      <stop offset="1" stop-color="var(--photo-ground)"/>
    </linearGradient>
  </defs>

  <rect class="banner-base" x="0" y="0" width="376" height="1180" fill="var(--brand-blue)"/>

  <g class="header">
    <text class="brand-name" x="188" y="134" text-anchor="middle">KELTO</text>
    <text class="tagline" x="188" y="168" text-anchor="middle">ROBOTICS | AUTOMATION | MECHATRONICS</text>
    <text class="tagline" x="188" y="188" text-anchor="middle">PROTOTYPING | SENSING</text>
    <text class="web-address" x="188" y="214" text-anchor="middle">keltolabworks.com</text>
  </g>

  <polygon class="services-panel" points="0,219 188,322 376,219 376,501 188,556 0,501" fill="var(--brand-red)"/>
  <polyline class="chevron-stripe" points="0,214 188,317 376,214" fill="none" stroke="var(--stripe-white)" stroke-width="8"/>

  <g class="services-list">
    <text class="services" x="188" y="365" text-anchor="middle">EMBEDDED ELECTRONICS AND</text>
    <text class="services" x="188" y="393" text-anchor="middle">CIRCUIT DESIGN</text>
    <text class="services" x="188" y="421" text-anchor="middle">RAPID FUNCTIONAL PROTOTYPING</text>
    <text class="services" x="188" y="449" text-anchor="middle">SENSOR AND VISION SYSTEMS</text>
    <text class="services" x="188" y="477" text-anchor="middle">ROBOTICS SYSTEMS</text>
  </g>

  <g class="team-photo" role="img" aria-label="Photo of the engineering team in hi-vis vests testing a robotic sewer probe over a concrete manhole beside a work truck">
    <polygon points="0,510 188,566 376,510 376,846 188,904 0,846" fill="url(#photoTones)"/>
  </g>

  <polyline class="chevron-stripe" points="0,851 188,909 376,851" fill="none" stroke="var(--brand-red)" stroke-width="6"/>
  <polyline class="chevron-stripe" points="0,858 188,916 376,858" fill="none" stroke="var(--stripe-white)" stroke-width="6"/>

  <g class="projects-list">
    <text class="projects" x="188" y="972" text-anchor="middle">Recent Projects Include:</text>
    <text class="projects" x="188" y="1000" text-anchor="middle">Robotic concrete sewer probes</text>
    <text class="projects" x="188" y="1028" text-anchor="middle">IoT wildlife tracking systems</text>
    <text class="projects" x="188" y="1058" text-anchor="middle">Robots for exploring wombat burrows</text>
    <text class="projects" x="188" y="1086" text-anchor="middle">Smart pest control technology</text>
  </g>

  <g class="grommets" fill="var(--grommet)">
    <circle cx="10" cy="10" r="3"/>
    <circle cx="366" cy="10" r="3"/>
    <circle cx="10" cy="1170" r="3"/>
    <circle cx="366" cy="1170" r="3"/>
  </g>
</svg>
</body>
</html>
```